Commercial janitorial cleaning

Janitorial cleaning particularly for commercial buildings. Website needs to specify free estimates. Location of service is Hudson, Valatie, East Greenbush, Troy, Albany ny area. Services page with Janitorial services- General Office Cleaning, Construction Cleaning, Carpet Extraction, Consultation/Business, Lighting Maintenance, Seasonal Deep Cleaning, Window cleaning, Event Cleaning, Floor and Carpet Cleaning, Floor Striping and Waxing. Contact us page with email phone number on page and a request page that emails me if they have any questions. About us page-the picture of my family on it with a section I can type a story myself.

Target Market(s)

Commercial businesses

Industry/Entity Type

Janitorial Service

Number of Pages Required

4 page

Font styles to use
Serif
Sans Serif
Script

Colors
ec1f27
1b1b1b
ffffff
9d9d9d

Requirements
Must have
• Phone number 555-304-7162. Must have free estimates on home page. Going for industrial / modern look to website
Nice to have
• Logo is a red and black building so if those colors could be coordinated to website that would be awesome.

```html
<!DOCTYPE html>
<html lang="en">
<head>
<meta charset="utf-8">
<title>Reliant Cleaning Services</title>
<link href="https://fonts.googleapis.com/css2?family=Raleway:wght@400;500;600;700;800&family=Lato:ital,wght@0,400;0,700;1,400&display=swap" rel="stylesheet">
<style>
:root{
  --red:#ec1f27;
  --ink:#1b1b1b;
  --white:#ffffff;
  --grey:#9d9d9d;
  --light:#f4f4f4;
  --map:#e2e2e2;
  --footer:#141b23;
  --text:#666666;
}
*{box-sizing:border-box;margin:0;padding:0}
html,body{width:1200px;height:3371px;overflow:hidden}
body{position:relative;background:var(--white);font-family:"Lato",sans-serif;color:var(--ink)}
.abs{position:absolute}
.heading{font-family:"Raleway",sans-serif;font-weight:700;font-size:34px;text-transform:uppercase;letter-spacing:.5px}
.heading .accent{color:var(--red)}

/* header */
.site-header{left:0;top:0;width:1200px;height:135px;background:var(--white);box-shadow:0 2px 6px rgba(0,0,0,.12);z-index:2}
.brand{left:99px;top:20px;display:flex;align-items:center;gap:14px}
.brand-mark{width:86px;height:86px;background:var(--red)}
.brand-name{font-family:"Raleway",sans-serif;font-weight:700;font-size:21px;line-height:25px;color:var(--red)}
.topbar{left:393px;top:0;width:720px;height:48px;background:var(--red);clip-path:polygon(22px 0,100% 0,100% 100%,0 100%);display:flex;align-items:center;color:var(--white);font-size:15px}
.topbar .item{display:flex;align-items:center;gap:10px;margin-left:92px}
.estimate-tab{left:912px;top:0;width:201px;height:48px;background:var(--ink);color:var(--white);font-family:"Raleway",sans-serif;font-weight:700;font-size:17px;display:flex;align-items:center;justify-content:center;clip-path:polygon(18px 0,100% 0,100% 100%,0 100%)}
.main-nav{left:535px;top:80px;display:flex;font-family:"Raleway",sans-serif;font-size:14px;font-weight:500}
.main-nav a{color:var(--ink);text-decoration:none;text-transform:uppercase;padding:0 20px;height:55px;position:relative}
.main-nav a.active{color:var(--red);font-weight:700}
.main-nav a.active::after{content:"";position:absolute;left:0;right:0;bottom:0;height:4px;background:var(--red)}

/* hero */
.hero{left:0;top:135px;width:1200px;height:472px;background:linear-gradient(135deg,#4a4a4a,#2b2b2b 45%,#5a5234 75%,#3a3a3a)}
.hero-shade{left:0;top:135px;width:1200px;height:472px;background:rgba(0,0,0,.35)}
.hero-title{left:0;top:290px;width:1200px;text-align:center;color:var(--white);font-family:"Raleway",sans-serif;font-weight:700;font-size:34px}
.hero-sub{left:0;top:352px;width:1200px;text-align:center;color:var(--white);font-size:19px}
.btn-red{background:var(--red);color:var(--white);font-family:"Raleway",sans-serif;font-weight:700;text-transform:uppercase;display:flex;align-items:center;justify-content:center}
.hero-btn{left:514px;top:406px;width:172px;height:44px;font-size:16px}
.hero-arrow{top:338px}

/* about */
.about-title{left:99px;top:648px}
.title-rule{height:2px;background:#d8d8d8}
.about-quote{left:99px;top:731px;width:630px;font-style:italic;font-size:16px;line-height:24px;color:#333}
.about-text{left:99px;width:630px;font-size:13px;line-height:22px;color:var(--text)}
.about-btn{top:1001px;height:43px;width:137px;font-size:13px}
.btn-outline{left:243px;background:var(--white);border:2px solid var(--red);color:var(--red)}
.about-photo{left:780px;top:652px;width:314px;height:382px;background:linear-gradient(160deg,#5b7a4a,#9aa985 40%,#6f7d8e 75%,#3e4a55);box-shadow:8px 8px 0 #e3e3e3}

/* services */
.services{left:0;top:1085px;width:1200px;height:893px;background:var(--light)}
.services-title{left:0;top:1122px;width:1200px;text-align:center}
.hex{width:236px;height:272px}
.hex svg{position:absolute;left:0;top:0}
.hex-label{position:absolute;left:0;top:172px;width:236px;text-align:center;color:var(--white);font-family:"Raleway",sans-serif;font-weight:700;font-size:19px;line-height:24px;text-shadow:0 1px 3px rgba(0,0,0,.7)}

/* testimonial */
.testimonial{left:0;top:1978px;width:1200px;height:408px;background:linear-gradient(90deg,#e33a40,#ec4a50 50%,#e0353b)}
.testimonial-title{left:0;top:2016px;width:1200px;text-align:center;color:var(--white)}
.avatar{left:99px;width:56px;height:62px;border:3px solid var(--white);background:linear-gradient(#c9a68e,#7e6a60)}
.quote-box{left:209px;top:2114px;width:892px;height:196px;border:1px solid rgba(255,255,255,.75);color:var(--white);text-align:center;font-size:13px;line-height:25px;padding:46px 60px 0}
.quote-icon{left:575px;top:2094px;width:52px;height:40px;background:#e8434a;display:flex;align-items:center;justify-content:center}
.quote-author{font-weight:700;margin-top:4px;display:block}

/* locations */
.locations{left:0;top:2386px;width:1200px;height:441px;background:var(--map)}
.world-map{left:80px;top:2400px;width:1040px;height:420px;background:radial-gradient(ellipse at 30% 45%,#cfcfcf 0,transparent 45%),radial-gradient(ellipse at 65% 40%,#cfcfcf 0,transparent 50%),radial-gradient(ellipse at 85% 80%,#d2d2d2 0,transparent 20%)}
.locations-title{left:0;top:2422px;width:1200px;text-align:center}
.pin{display:flex;flex-direction:column;align-items:center;color:var(--red);font-family:"Raleway",sans-serif;font-weight:700;font-size:18px;width:200px;margin-left:-100px}

/* footer */
.site-footer{left:0;top:2827px;width:1200px;height:544px;background:var(--footer)}
.footer-nav{left:99px;top:2868px;width:1002px;display:flex;justify-content:space-around;font-family:"Raleway",sans-serif;font-size:16px;text-transform:uppercase;color:var(--white)}
.footer-nav .sep{color:#555}
.footer-rule{left:99px;top:2923px;width:1002px;height:1px;background:#3a434d}
.footer-heading{font-family:"Raleway",sans-serif;font-weight:500;font-size:20px;text-transform:uppercase;letter-spacing:.5px;color:var(--white)}
.field{left:99px;width:321px;height:32px;border:1px solid #6a737c;font-size:13px;padding:8px 14px;color:#d8d8d8}
.submit-btn{left:99px;top:3245px;width:137px;height:42px;font-size:16px}
.footer-brand{left:440px;top:3150px;width:320px;text-align:center;font-family:"Raleway",sans-serif;font-weight:700;font-size:26px;line-height:33px;color:var(--white)}
.footer-brand-mark{left:555px;top:3020px;width:90px;height:90px;background:var(--white)}
.contact-row{left:777px;display:flex;gap:16px;font-size:13px;line-height:19px;color:var(--white)}
.contact-icon{width:30px;height:30px;border:2px solid var(--white);border-radius:50%;flex:none;display:flex;align-items:center;justify-content:center}
.contact-row b{font-weight:700;display:block}
.follow{left:780px;top:3232px;font-size:14px;font-weight:700;color:var(--white)}
.social{left:780px;top:3263px;display:flex;gap:9px}
.social span{width:24px;height:24px;display:block}
.copyright{left:0;top:3323px;width:1200px;text-align:center;font-size:13px;color:#cfd3d7}
</style>
</head>
<body>

<header class="abs site-header">
  <div class="abs brand">
    <span class="brand-mark"></span>
    <span class="brand-name">Reliant<br>Cleaning Services</span>
  </div>
  <div class="abs topbar">
    <span class="item">
      <svg width="18" height="14" viewBox="0 0 18 14"><rect x="1" y="1" width="16" height="12" fill="none" stroke="#fff" stroke-width="1.6"/><path d="M1 1l8 7 8-7" fill="none" stroke="#fff" stroke-width="1.6"/></svg>
      hello@reliantcleaning.com
    </span>
    <span class="item" style="margin-left:40px">
      <svg width="16" height="16" viewBox="0 0 16 16"><path d="M3 1l3 3-2 2c1 2 3 4 5 5l2-2 3 3-2 3C6 15 1 10 1 3z" fill="none" stroke="#fff" stroke-width="1.4"/></svg>
      555-304-7162
    </span>
  </div>
  <div class="abs estimate-tab">FREE ESTIMATE</div>
  <nav class="abs main-nav">
    <a class="active">Home</a><a>About Us</a><a>Our Services</a><a>Our Location</a><a>Contact</a>
  </nav>
</header>

<section>
  <div class="abs hero" role="img" aria-label="Office lobby floor with a yellow wet floor caution sign"></div>
  <div class="abs hero-shade"></div>
  <h1 class="abs hero-title">RELIANT CLEANING SERVICES</h1>
  <p class="abs hero-sub">We Are Specialized In Janitorial Cleaning Particularly For Commercial Buildings.</p>
  <div class="abs btn-red hero-btn">Free Estimate</div>
  <svg class="abs hero-arrow" style="left:48px" width="34" height="64" viewBox="0 0 34 64"><path d="M32 2L2 32l30 30" fill="none" stroke="#fff" stroke-width="2.5"/></svg>
  <svg class="abs hero-arrow" style="left:1118px" width="34" height="64" viewBox="0 0 34 64"><path d="M2 2l30 30L2 62" fill="none" stroke="#fff" stroke-width="2.5"/></svg>
</section>

<section>
  <h2 class="abs heading about-title"><span class="accent">About</span> Us</h2>
  <div class="abs title-rule" style="left:99px;top:699px;width:630px"></div>
  <div class="abs" style="left:99px;top:697px;width:120px;height:4px;background:var(--red)"></div>
  <p class="abs about-quote">“Neque porro quisquam est qui dolorem ipsum quia dolor sit amet, consectetur, ipisci velit There is no one who loves.”</p>
  <p class="abs about-text" style="top:793px">Lorem Ipsum is simply dummy text of the printing and typesetting industry. Lorem Ipsum has been the industry's standard dummy text ever since the 1500s, when an unknown printer took a galley of type and scrambled it to make a type specimen book. It has survived not only five centuries, but also the leap into electronic typesetting, remaining essentiall.</p>
  <p class="abs about-text" style="top:905px">Lorem Ipsum is simply dummy text of the printing and typesetting industry. Lorem Ipsum has been the industry's standard dummy text ever since the 1500s, when an unknown printer took a galley of type and scrambled it to make a type specimen book. It has survived not only five centuries.</p>
  <div class="abs btn-red about-btn" style="left:99px">Read More</div>
  <div class="abs btn-red about-btn btn-outline">Contact Us</div>
  <div class="abs about-photo" role="img" aria-label="Family photo on a ladder outdoors"></div>
</section>

<section>
  <div class="abs services"></div>
  <h2 class="abs heading services-title"><span class="accent">Our</span> Service</h2>
  <div class="abs title-rule" style="left:430px;top:1176px;width:340px"></div>

  <svg width="0" height="0" style="position:absolute">
    <defs>
      <linearGradient id="hexFill" x1="0" y1="0" x2="0" y2="1">
        <stop offset="0" stop-color="#9a9a9a"/><stop offset=".55" stop-color="#6b6b6b"/><stop offset="1" stop-color="#2e2e2e"/>
      </linearGradient>
    </defs>
  </svg>

  <div class="abs hex" style="left:230px;top:1205px" role="img" aria-label="Office waiting area being cleaned"><svg width="236" height="272" viewBox="0 0 236 272"><polygon points="118,6 230,70 230,202 118,266 6,202 6,70" fill="url(#hexFill)" stroke="#ec1f27" stroke-width="9"/></svg><div class="hex-label">General Office<br>Cleaning</div></div>
  <div class="abs hex" style="left:484px;top:1205px" role="img" aria-label="Worker in hard hat cleaning a construction site"><svg width="236" height="272" viewBox="0 0 236 272"><polygon points="118,6 230,70 230,202 118,266 6,202 6,70" fill="url(#hexFill)" stroke="#ec1f27" stroke-width="9"/></svg><div class="hex-label">Construction<br>Cleaning</div></div>
  <div class="abs hex" style="left:738px;top:1205px" role="img" aria-label="Carpet extraction machine in use"><svg width="236" height="272" viewBox="0 0 236 272"><polygon points="118,6 230,70 230,202 118,266 6,202 6,70" fill="url(#hexFill)" stroke="#ec1f27" stroke-width="9"/></svg><div class="hex-label">Carpet<br>Extraction</div></div>

  <div class="abs hex" style="left:100px;top:1430px" role="img" aria-label="Worker moving boxes in a business space"><svg width="236" height="272" viewBox="0 0 236 272"><polygon points="118,6 230,70 230,202 118,266 6,202 6,70" fill="url(#hexFill)" stroke="#ec1f27" stroke-width="9"/></svg><div class="hex-label">Construction/<br>Business</div></div>
  <div class="abs hex" style="left:356px;top:1430px" role="img" aria-label="Workers servicing ceiling lights"><svg width="236" height="272" viewBox="0 0 236 272"><polygon points="118,6 230,70 230,202 118,266 6,202 6,70" fill="url(#hexFill)" stroke="#ec1f27" stroke-width="9"/></svg><div class="hex-label">Lighting<br>Maintenance</div></div>
  <div class="abs hex" style="left:612px;top:1430px" role="img" aria-label="Person wiping a surface"><svg width="236" height="272" viewBox="0 0 236 272"><polygon points="118,6 230,70 230,202 118,266 6,202 6,70" fill="url(#hexFill)" stroke="#ec1f27" stroke-width="9"/></svg><div class="hex-label">Seasonal Deep<br>Cleaning</div></div>
  <div class="abs hex" style="left:868px;top:1430px" role="img" aria-label="Window cleaner on a lift outside a glass building"><svg width="236" height="272" viewBox="0 0 236 272"><polygon points="118,6 230,70 230,202 118,266 6,202 6,70" fill="url(#hexFill)" stroke="#ec1f27" stroke-width="9"/></svg><div class="hex-label">Window<br>Cleaning</div></div>

  <div class="abs hex" style="left:230px;top:1655px" role="img" aria-label="Broom sweeping confetti after an event"><svg width="236" height="272" viewBox="0 0 236 272"><polygon points="118,6 230,70 230,202 118,266 6,202 6,70" fill="url(#hexFill)" stroke="#ec1f27" stroke-width="9"/></svg><div class="hex-label">Event<br>Cleaning</div></div>
  <div class="abs hex" style="left:484px;top:1655px" role="img" aria-label="Carpet being cleaned in an office"><svg width="236" height="272" viewBox="0 0 236 272"><polygon points="118,6 230,70 230,202 118,266 6,202 6,70" fill="url(#hexFill)" stroke="#ec1f27" stroke-width="9"/></svg><div class="hex-label">Floor &amp; Carpet<br>Cleaning</div></div>
  <div class="abs hex" style="left:738px;top:1655px" role="img" aria-label="Floor buffing machine on a polished floor"><svg width="236" height="272" viewBox="0 0 236 272"><polygon points="118,6 230,70 230,202 118,266 6,202 6,70" fill="url(#hexFill)" stroke="#ec1f27" stroke-width="9"/></svg><div class="hex-label">Floor Striping<br>&amp; Waxing</div></div>
</section>

<section>
  <div class="abs testimonial" role="img" aria-label="Blurred red tinted office background"></div>
  <h2 class="abs heading testimonial-title" style="font-weight:600">Client Testimonial</h2>
  <div class="abs" style="left:430px;top:2070px;width:340px;height:1px;background:rgba(255,255,255,.6)"></div>
  <div class="abs avatar" style="top:2113px" role="img" aria-label="Client portrait"></div>
  <div class="abs avatar" style="top:2184px" role="img" aria-label="Client portrait"></div>
  <div class="abs avatar" style="top:2255px" role="img" aria-label="Client portrait"></div>
  <div class="abs quote-box">
    Lorem Ipsum is simply dummy text of the printing and typesetting industry. Lorem Ipsum has been the industry's standard dummy text ever since the 1500s, when an unknown printer took a galley of type and scrambled it to make a type specimen book. It has survived not only five centuries, but mmy text ever since the 1500s, when an unknown printer took a galley of type and scramblalso the leap into electronic typesetting, remaining essentiall.
    <span class="quote-author">- Mr. Lorem Ipsum, Company Name</span>
  </div>
  <div class="abs quote-icon">
    <svg width="40" height="34" viewBox="0 0 40 34"><path d="M4 3h32v20H16l-8 8v-8H4z" fill="none" stroke="#fff" stroke-width="2.4"/><path d="M11 11h18M11 16h14" stroke="#fff" stroke-width="2"/></svg>
  </div>
</section>

<section>
  <div class="abs locations"></div>
  <div class="abs world-map" role="img" aria-label="World map outline in light grey"></div>
  <h2 class="abs heading locations-title"><span class="accent">Location of</span> Service</h2>
  <div class="abs title-rule" style="left:410px;top:2474px;width:380px;background:#c8c8c8"></div>
  <div class="abs pin" style="left:418px;top:2540px"><svg width="16" height="22" viewBox="0 0 16 22"><path d="M8 1a7 7 0 00-7 7c0 5 7 13 7 13s7-8 7-13a7 7 0 00-7-7z" fill="#ec1f27"/><circle cx="8" cy="8" r="2.6" fill="#fff"/></svg>Hudson</div>
  <div class="abs pin" style="left:687px;top:2540px"><svg width="16" height="22" viewBox="0 0 16 22"><path d="M8 1a7 7 0 00-7 7c0 5 7 13 7 13s7-8 7-13a7 7 0 00-7-7z" fill="#ec1f27"/><circle cx="8" cy="8" r="2.6" fill="#fff"/></svg>Valatie</div>
  <div class="abs pin" style="left:580px;top:2612px"><svg width="16" height="22" viewBox="0 0 16 22"><path d="M8 1a7 7 0 00-7 7c0 5 7 13 7 13s7-8 7-13a7 7 0 00-7-7z" fill="#ec1f27"/><circle cx="8" cy="8" r="2.6" fill="#fff"/></svg>Albany</div>
  <div class="abs pin" style="left:423px;top:2674px"><svg width="16" height="22" viewBox="0 0 16 22"><path d="M8 1a7 7 0 00-7 7c0 5 7 13 7 13s7-8 7-13a7 7 0 00-7-7z" fill="#ec1f27"/><circle cx="8" cy="8" r="2.6" fill="#fff"/></svg>Troy</div>
  <div class="abs pin" style="left:818px;top:2654px"><svg width="16" height="22" viewBox="0 0 16 22"><path d="M8 1a7 7 0 00-7 7c0 5 7 13 7 13s7-8 7-13a7 7 0 00-7-7z" fill="#ec1f27"/><circle cx="8" cy="8" r="2.6" fill="#fff"/></svg>East Greenbush</div>
</section>

<footer>
  <div class="abs site-footer"></div>
  <nav class="abs footer-nav">
    <span>Home</span><span class="sep">|</span><span>About Us</span><span class="sep">|</span><span>Our Services</span><span class="sep">|</span><span>Our Location</span><span class="sep">|</span><span>Contact</span>
  </nav>
  <div class="abs footer-rule"></div>

  <h3 class="abs footer-heading" style="left:99px;top:2964px">Quick Inquiry</h3>
  <div class="abs field" style="top:3018px">Name</div>
  <div class="abs field" style="top:3065px">Email</div>
  <div class="abs field" style="top:3112px">Phone</div>
  <div class="abs field" style="top:3159px;height:70px">Message</div>
  <div class="abs btn-red submit-btn">Submit</div>

  <div class="abs footer-brand-mark"></div>
  <div class="abs footer-brand">Reliant<br>Cleaning Services</div>

  <h3 class="abs footer-heading" style="left:777px;top:2964px">Contact Details</h3>
  <div class="abs contact-row" style="top:3020px">
    <span class="contact-icon"><svg width="12" height="16" viewBox="0 0 12 16"><path d="M6 1a5 5 0 00-5 5c0 4 5 9 5 9s5-5 5-9a5 5 0 00-5-5z" fill="#fff"/></svg></span>
    <span><b>Reliant Cleaning Services</b>Lorem Ipsum is simply dummy text of the<br>printing and typesetting industry.</span>
  </div>
  <div class="abs contact-row" style="top:3100px">
    <span class="contact-icon"><svg width="14" height="10" viewBox="0 0 14 10"><rect x="1" y="1" width="12" height="8" fill="none" stroke="#fff" stroke-width="1.4"/><path d="M1 1l6 5 6-5" fill="none" stroke="#fff" stroke-width="1.4"/></svg></span>
    <span><b>EMAIL</b>hello@reliantcleaning.com</span>
  </div>
  <div class="abs contact-row" style="top:3160px">
    <span class="contact-icon"><svg width="14" height="14" viewBox="0 0 16 16"><path d="M3 1l3 3-2 2c1 2 3 4 5 5l2-2 3 3-2 3C6 15 1 10 1 3z" fill="#fff"/></svg></span>
    <span><b>CALL US</b>555-304-7162</span>
  </div>
  <div class="abs follow">FOLLOW US:</div>
  <div class="abs social">
    <span style="background:#3b5a98"></span><span style="background:#1f7bb6"></span><span style="background:#2aa4dd"></span><span style="background:#dd4b39"></span>
  </div>
  <p class="abs copyright">Copyright © 2017 Reliant Cleaning Services. All Rights Reserved.</p>
</footer>

</body>
</html>
```